VERIDAX Need a luxury modern business card designed.

Need a luxury modern business card designed. refer to the uploaded files for the company name and logo in the zip file under source files. i will making my descion on monday. so please send in before then so if we need to edit we will have the time. we have a trade show coming up and im on a deadline for printer.

Target Market(s)

high end clients

Contact Information for Business Card

Company nAme and logo. Calvin Ostrow Co-Founder / Project Manager Office # 416-555-0193 Cell # 416-555-0147 VERIDAX.CA Calvin@veridax.ca

Font styles to use
Other font styles liked:
• Modern

Requirements
Must have
• Company name and logo, contact info, using the black, gold and white color scheme.

```html
<!DOCTYPE html>
<html lang="en">
<head>
<meta charset="utf-8">
<title>VERIDAX Business Card</title>
<link rel="stylesheet" href="https://fonts.googleapis.com/css2?family=Poppins:wght@300;400;500&display=swap">
<style>
  :root {
    --charcoal: #2f2f30;
    --ink: #1f1f20;
    --gold: #a8976a;
    --white: #ffffff;
    --grey: #8a8a8a;
    --stage: #1a1a1a;
  }
  * { box-sizing: border-box; margin: 0; padding: 0; }
  html, body { width: 1200px; height: 880px; overflow: hidden; }
  body {
    background: var(--stage);
    font-family: "Poppins", sans-serif;
    position: relative;
  }
  .card {
    position: absolute;
    left: 320px;
    width: 560px;
    height: 320px;
    border-radius: 22px;
    overflow: hidden;
    background: var(--charcoal);
  }
  .card--front { top: 100px; }
  .card--back { top: 460px; }

  .brand {
    position: absolute;
    display: flex;
    flex-direction: column;
    align-items: center;
  }
  .brand__row { display: flex; align-items: center; gap: 16px; }
  .brand__square { width: 34px; height: 34px; background: var(--gold); flex: none; }
  .brand__name {
    font-weight: 300;
    font-size: 48px;
    letter-spacing: 8px;
    line-height: 1;
  }
  .brand__tagline {
    display: flex;
    align-items: center;
    gap: 10px;
    margin-top: 12px;
    font-size: 10px;
    letter-spacing: 4px;
    font-weight: 400;
  }
  .brand__rule { width: 40px; height: 1px; }

  .card--front .brand { left: 0; right: 0; top: 114px; }
  .card--front .brand__name { color: var(--white); }
  .card--front .brand__tagline { color: var(--gold); }
  .card--front .brand__rule { background: var(--grey); }

  .back-shape { position: absolute; inset: 0; }
  .card--back .brand { left: 18px; width: 250px; top: 128px; }
  .card--back .brand__row { gap: 12px; }
  .card--back .brand__name { color: var(--ink); font-size: 32px; letter-spacing: 5px; }
  .card--back .brand__square { width: 24px; height: 24px; }
  .card--back .brand__tagline { color: var(--grey); font-size: 8px; letter-spacing: 3px; margin-top: 9px; }
  .card--back .brand__rule { background: var(--grey); width: 26px; }

  .contact {
    position: absolute;
    left: 330px;
    top: 56px;
    color: var(--white);
  }
  .contact__name { font-size: 22px; font-weight: 400; letter-spacing: 0.5px; line-height: 1.1; }
  .contact__name .surname { color: var(--gold); }
  .contact__title { font-size: 11px; color: var(--grey); font-weight: 300; margin-top: 3px; }
  .contact__list { list-style: none; margin-top: 18px; }
  .contact__item {
    display: flex; align-items: center; gap: 10px;
    font-size: 12.5px; font-weight: 300; line-height: 20px;
  }
  .contact__item svg { width: 12px; height: 12px; flex: none; }
  .contact__address { margin-top: 16px; font-size: 12.5px; font-weight: 300; line-height: 19px; padding-left: 22px; }
</style>
</head>
<body>

  <section class="card card--front" aria-label="Card front">
    <div class="brand">
      <div class="brand__row">
        <span class="brand__square"></span>
        <span class="brand__name">VERIDAX</span>
      </div>
      <div class="brand__tagline">
        <span class="brand__rule"></span>LUXURY LANDSCAPES<span class="brand__rule"></span>
      </div>
    </div>
  </section>

  <section class="card card--back" aria-label="Card back">
    <svg class="back-shape" viewBox="0 0 560 320" preserveAspectRatio="none" aria-hidden="true">
      <rect width="560" height="320" fill="var(--charcoal)"/>
      <path d="M0 0 H246 Q330 140 300 320 H0 Z" fill="var(--gold)"/>
      <path d="M0 0 H240 Q318 140 284 320 H0 Z" fill="var(--white)"/>
    </svg>

    <div class="brand">
      <div class="brand__row">
        <span class="brand__square"></span>
        <span class="brand__name">VERIDAX</span>
      </div>
      <div class="brand__tagline">
        <span class="brand__rule"></span>LUXURY LANDSCAPES<span class="brand__rule"></span>
      </div>
    </div>

    <div class="contact">
      <p class="contact__name">CALVIN <span class="surname">OSTROW</span></p>
      <p class="contact__title">Co-Founder / Project Manager</p>
      <ul class="contact__list">
        <li class="contact__item">
          <svg viewBox="0 0 12 12"><path d="M1 4 Q6 0 11 4 L9 5.5 L8 4 H4 L3 5.5 Z M3 6 H9 L10 11 H2 Z" fill="var(--gold)"/></svg>
          416-555-0193
        </li>
        <li class="contact__item">
          <svg viewBox="0 0 12 12"><rect x="3" y="1" width="6" height="10" rx="1" fill="none" stroke="var(--gold)" stroke-width="1.2"/></svg>
          416-555-0147
        </li>
        <li class="contact__item">
          <svg viewBox="0 0 12 12"><circle cx="6" cy="6" r="5" fill="none" stroke="var(--gold)"/><ellipse cx="6" cy="6" rx="2.2" ry="5" fill="none" stroke="var(--gold)"/><path d="M1 6 H11" stroke="var(--gold)"/></svg>
          VERIDAX.CA
        </li>
        <li class="contact__item">
          <svg viewBox="0 0 12 12"><rect x="1" y="2.5" width="10" height="7" fill="var(--gold)"/><path d="M1 2.5 L6 6.5 L11 2.5" fill="none" stroke="var(--charcoal)"/></svg>
          Calvin@veridax.ca
        </li>
      </ul>
      <p class="contact__address">88 Harlow Road, Unit 5,<br>Concord, ON. L4K 0Z9</p>
    </div>
  </section>

</body>
</html>
```